【タイトル】
超現実派エンジニアも驚く!
メンタル不調も!恋愛の失敗も!実らない努力も!

全ての原因は56種の「モヤリンk」
最強ワークで過去を手放し、人生を全て好転させよう! 

【書籍の特典情報】
誰でもできる
「セルフ解放ワーク」
の動画プレゼント!

【ターゲット】
引き寄せの法則や成功法則が好きな方向け

【著者】
(元システムエンジニア)
企業サポーター
桐野 沙織

【説明】
電子書籍の表紙のデザインをお願いします。

電子書籍なので、タイトル文字を見やすくしてほしいです。

元システムエンジニアで、企業サポーターという職業柄もあり
とても現実派の私が実感して提供しているワークのお話になります

引き寄せやスピリチュアルとは違うので、
どちらかというと成功の法則のように
現実的なイメージの表紙だと良いかなと思っています。

本文をつけますので参考にしていただければと思います。

見た時に、とてもインパクトがあるように感じました。
電子書籍は、表紙の役割が大きいので
わかりやすさもとても大切だと感じ、選ばせていただきました。

皆様、素敵なデザインをご提案いただきありがとうございます。
とても迷い、投票も行い選択させていただきました。
今後、お仕事やデザインをご依頼させていただく際は
また、よろしくお願いいたします。

```html
<!DOCTYPE html>
<html lang="ja">
<head>
<meta charset="UTF-8">
<title>全ての原因は56種の「モヤリンk」</title>
<link rel="stylesheet" href="https://fonts.googleapis.com/css2?family=Noto+Sans+JP:wght@500;700;900&display=swap">
<style>
  :root {
    --paper: #ffffff;
    --ink: #2b2b2b;
    --arrow-green: #c3df9c;
    --title-green: #2f6a1d;
    --band-green: #6fae2f;
    --band-green-dark: #4c8a1a;
    --accent-orange: #f08a1c;
    --figure-tone: #e9dcc7;
  }
  * { margin: 0; padding: 0; box-sizing: border-box; }
  html, body { width: 750px; height: 1200px; overflow: hidden; background: var(--paper); }
  body { font-family: "Noto Sans JP", sans-serif; color: var(--ink); }
  .cover { position: relative; width: 750px; height: 1200px; overflow: hidden; background: var(--paper); }

  .arrow-shape { position: absolute; left: 0; top: 0; width: 750px; height: 1200px; }

  .author { position: absolute; left: 36px; top: 22px; }
  .author-name { font-size: 40px; font-weight: 700; letter-spacing: 2px; }
  .author-name small { font-size: 24px; font-weight: 500; margin-left: 6px; }
  .author-role { font-size: 18px; font-weight: 500; line-height: 1.35; margin-top: 4px; }

  .couple-figure {
    position: absolute; left: 20px; top: 130px; width: 290px; height: 420px;
    border-radius: 40px;
    background: linear-gradient(180deg, var(--figure-tone), #f3ebdd);
  }

  .title-block {
    position: absolute; left: 330px; top: 345px;
    transform: rotate(-60deg); transform-origin: left top;
    white-space: nowrap;
  }
  .title-lead {
    display: inline-block; background: var(--paper); color: var(--title-green);
    font-size: 26px; font-weight: 900; padding: 2px 16px; border-radius: 30px;
    border: 3px solid var(--title-green); margin-bottom: 4px;
  }
  .title-line { display: block; font-size: 54px; font-weight: 900; color: var(--title-green); line-height: 1.28; }

  .green-band {
    position: absolute; left: 0; top: 575px; width: 750px; height: 450px;
    background: var(--band-green);
  }
  .cause { position: absolute; left: 40px; top: 600px; color: var(--paper); font-weight: 900; text-shadow: 3px 3px 0 var(--band-green-dark); }
  .cause-lead { display: block; font-size: 50px; line-height: 1.2; }
  .cause-main { display: block; font-size: 50px; line-height: 1.25; white-space: nowrap; }
  .cause-main .keyword { font-size: 76px; }

  .promise {
    position: absolute; left: 40px; top: 800px; color: var(--paper); font-weight: 900;
    font-size: 46px; line-height: 1.35; transform: rotate(-3deg); transform-origin: left top;
    text-shadow: 3px 3px 0 var(--band-green-dark); white-space: nowrap;
  }
  .promise .bang { font-size: 70px; color: #fff7a8; }

  .bonus { position: absolute; left: 0; top: 1025px; width: 750px; height: 175px; background: var(--paper); }
  .bonus-text { position: absolute; right: 150px; top: 22px; text-align: right; font-weight: 900; color: var(--ink); }
  .bonus-lead { display: block; font-size: 36px; line-height: 1.3; }
  .bonus-main { display: block; font-size: 44px; line-height: 1.3; white-space: nowrap; }
  .bonus-tag {
    position: absolute; right: 30px; top: 30px; width: 100px; padding: 8px 0;
    background: var(--accent-orange); color: var(--paper); font-size: 44px; font-weight: 900;
    text-align: center; line-height: 1.1; border-radius: 8px;
  }
  .bonus-rule { position: absolute; left: 0; bottom: 0; width: 750px; height: 16px; background: var(--accent-orange); }
</style>
</head>
<body>
<main class="cover">
  <svg class="arrow-shape" viewBox="0 0 750 1200" aria-hidden="true">
    <polygon fill="var(--arrow-green)" points="80,700 520,150 430,90 750,0 720,330 640,250 260,760"/>
  </svg>

  <header class="author">
    <p class="author-name">桐野 沙織<small>著</small></p>
    <p class="author-role">企業サポーター<br>(元システムエンジニア)</p>
  </header>

  <div class="couple-figure" role="img" aria-label="悩んだ表情の男女のイラスト"></div>

  <h1 class="title-block">
    <span class="title-lead">超現実派エンジニアも驚く!</span>
    <span class="title-line">メンタル不調も!</span>
    <span class="title-line">恋愛の失敗も!</span>
    <span class="title-line">実らない努力も!</span>
  </h1>

  <section class="green-band"></section>
  <p class="cause">
    <span class="cause-lead">全ての原因は</span>
    <span class="cause-main">56種の<span class="keyword">「モヤリンk」</span></span>
  </p>
  <p class="promise">最強ワークで過去を手放し、<br>人生を全て好転させよう<span class="bang">!</span></p>

  <section class="bonus">
    <p class="bonus-text">
      <span class="bonus-lead">誰でもできる</span>
      <span class="bonus-main">「セルフ解放ワーク」の動画</span>
    </p>
    <p class="bonus-tag">特<br>典</p>
    <div class="bonus-rule"></div>
  </section>
</main>
</body>
</html>
```